White Rum brand needs bottle label

Looking for a label that will stand out on a shelf and feel like an instant classic. Corvane is a premium Caribbean blended white rum that was crafted as an escape from day-to-day stress and is all about making each day feel as though it's a vacation day. It was named after two local beaches and surf breaks both of which are party towns. I'd like the label to feel modern, sleek, and casual, while still feeling very slightly upscale and have a few subtle hints of it's tropical origin. Corvane should look suitable to drink in variety of situations such as a casual drink at the beach or a pool, a cocktail after a long day of work, or a night out at a bar or club. Please incorporate the logo somewhere in the label, whether that's just the mermaid or the entire design I'll leave that up to the designer. Whatever it is, it should have a look that is scalable and feels appropriate to consume in many settings while remembering it's Carribean and beach roots.

Target Market(s)

The target market is fairly broad. Target consumers are between 21-55, leaning slightly more towards the masculine crowd, full-time workers that enjoy drinking regularly.

Font styles to use
Serif
Sans Serif

Requirements
Must have
• Must have at least the mermaid part of the logo incorporated within the label.
Nice to have
• I'd like a bottle with a synthetic cork, that has a strap sealer over the top and a bottle shaped similar to Valdoro Tequila. Colors are designer's choice. Subtle floral or tropical notes (not too much) mixed into a fairly sleek and modern design.

```html
<!DOCTYPE html>
<html lang="en">
<head>
<meta charset="utf-8">
<title>Corvane White Rum – Bottle Label</title>
<link rel="stylesheet" href="https://fonts.googleapis.com/css2?family=Montserrat:wght@600&family=Old+Standard+TT:wght@400;700&family=Ultra&family=Kaushan+Script&display=swap">
<style>
  :root {
    --backdrop: #0c0d0e;
    --label-black: #161616;
    --label-paper: #f4f4f2;
    --label-line: #b9b9b6;
    --gold: #d8c07a;
    --gold-deep: #b39a55;
    --gold-faint: #ece3c6;
    --ink: #1b1b1b;
  }
  html, body {
    margin: 0;
    padding: 0;
    width: 1200px;
    height: 1000px;
    overflow: hidden;
    background: var(--backdrop);
  }
  .canvas {
    position: relative;
    width: 1200px;
    height: 1000px;
  }
  .label-art { display: block; }
  .arc-tagline {
    font-family: "Montserrat", sans-serif;
    font-weight: 600;
    font-size: 13px;
    letter-spacing: 3px;
    fill: var(--ink);
  }
  .estd {
    font-family: "Montserrat", sans-serif;
    font-weight: 600;
    font-size: 10px;
    letter-spacing: 2px;
    fill: var(--gold-deep);
  }
  .brand-name {
    font-family: "Old Standard TT", serif;
    font-weight: 700;
    font-size: 80px;
    fill: var(--ink);
  }
  .variant {
    font-family: "Kaushan Script", cursive;
    font-size: 40px;
    fill: var(--gold);
  }
  .product {
    font-family: "Ultra", serif;
    font-size: 78px;
    letter-spacing: 18px;
    fill: var(--gold);
  }
  .spec-caption {
    font-family: "Old Standard TT", serif;
    font-size: 17px;
    letter-spacing: 1px;
    fill: var(--ink);
  }
  .spec-value {
    font-family: "Old Standard TT", serif;
    font-size: 52px;
    fill: var(--ink);
  }
</style>
</head>
<body>
<main class="canvas">
  <svg class="label-art" width="1200" height="1000" viewBox="0 0 1200 1000" xmlns="http://www.w3.org/2000/svg">
    <defs>
      <path id="tagline-arc" d="M 506 334 A 100 100 0 1 1 694 334"/>
    </defs>

    <g class="label-frame">
      <polygon points="600,88 878,164 878,836 600,912 322,836 322,164" fill="var(--label-black)"/>
      <polygon points="600,100 866,172 866,828 600,900 334,828 334,172" fill="none" stroke="var(--gold)" stroke-width="3"/>
      <polygon points="600,114 852,182 852,818 600,886 348,818 348,182" fill="var(--label-paper)"/>
      <polygon points="600,128 838,192 838,808 600,872 362,808 362,192" fill="none" stroke="var(--label-line)" stroke-width="2"/>
    </g>

    <rect class="bottle-motif" role="img" aria-label="Faint bottle silhouette decoration" x="392" y="250" width="86" height="220" rx="30" fill="var(--gold-faint)" opacity="0.7"/>

    <g class="emblem">
      <text class="arc-tagline"><textPath href="#tagline-arc" startOffset="50%" text-anchor="middle">PREMIUM CARIBBEAN BLENDED</textPath></text>
      <circle class="emblem-mark" role="img" aria-label="Mermaid emblem area" cx="600" cy="290" r="52" fill="var(--gold)" opacity="0.55"/>
      <text class="estd" x="528" y="308" text-anchor="middle">ESTD</text>
      <text class="estd" x="672" y="308" text-anchor="middle">2021</text>
    </g>

    <text class="brand-name" x="600" y="420" text-anchor="middle">Corvane</text>

    <g class="ribbon">
      <polygon points="322,505 262,485 292,555 252,625 340,627" fill="var(--gold)"/>
      <polygon points="878,505 938,485 908,555 948,625 860,627" fill="var(--gold)"/>
      <path d="M 300 480 Q 600 440 900 480 L 900 630 Q 600 590 300 630 Z" fill="var(--label-black)"/>
      <path d="M 300 488 Q 600 448 900 488" fill="none" stroke="var(--gold)" stroke-width="2"/>
      <path d="M 300 622 Q 600 582 900 622" fill="none" stroke="var(--gold)" stroke-width="2"/>
    </g>

    <text class="variant" x="600" y="506" text-anchor="middle">White</text>
    <text class="product" x="609" y="592" text-anchor="middle">RUM</text>

    <g class="specs">
      <text class="spec-caption" x="500" y="680" text-anchor="middle">VOL (ML)</text>
      <text class="spec-value" x="500" y="736" text-anchor="middle">750</text>
      <line x1="600" y1="662" x2="600" y2="746" stroke="var(--ink)" stroke-width="2"/>
      <text class="spec-caption" x="700" y="680" text-anchor="middle">ALC/VOL</text>
      <text class="spec-value" x="700" y="736" text-anchor="middle">43%</text>
    </g>
  </svg>
</main>
</body>
</html>
```